Flyer Mail out

Need something urgently designed.

I need a flyer done double sided I have provided CWDG photos and the writing. I do not have any dental surgery stock photos as such but this can be used. We are a mobile dental company that goes out to schools and provide free dental services.

I have attached the written document and would like it double sided A4 paper.

The colours I want is Aqua, Light Blue, dark blue, grey and white.

Just need it designed beautifully and professionally to go out to principals to contact us and use our services.

If you would like more info have a look at our Chatterloop page Coastline Wandering Dental Group

```html
<!DOCTYPE html>
<html lang="en">
<head>
<meta charset="utf-8">
<title>Coastline Wandering Dental Group – Principal Flyer</title>
<link href="https://fonts.googleapis.com/css2?family=Barlow:wght@300;400;600&display=swap" rel="stylesheet">
<style>
  :root {
    --aqua: #6dcde2;
    --navy: #0e3a63;
    --sky: #2f8fd0;
    --grey: #e6e6e6;
    --ink: #2c4a6b;
    --white: #ffffff;
    --guide: #d6338a;
    --label: #222222;
  }
  html, body { margin: 0; padding: 0; overflow: hidden; background: var(--white); }
  .sheet {
    position: relative; width: 726px; height: 1200px; overflow: hidden;
    font-family: "Barlow", Arial, sans-serif; color: var(--ink);
  }
  .side-label {
    position: absolute; left: 0; width: 726px; text-align: center;
    font-weight: 300; font-size: 22px; letter-spacing: 1px; color: var(--label);
  }
  .abs { position: absolute; }
  .guide { position: absolute; border: 1px solid var(--guide); box-sizing: border-box; pointer-events: none; }
  .guide-v { position: absolute; width: 0; border-left: 1px solid var(--guide); }

  /* front */
  .letter { left: 32px; top: 94px; width: 272px; font-size: 6.9px; line-height: 8.1px; font-weight: 400; }
  .letter h1 { margin: 0 0 6px; font-size: 12px; font-weight: 600; color: var(--sky); }
  .letter p { margin: 0; }
  .letter .gap { margin-top: 8px; }
  .photo { background: linear-gradient(135deg, #f2c4b2 0%, #e39a8a 45%, #b2453e 70%, #f5e6e0 100%); }
  .brand-box {
    left: 387px; top: 448px; width: 247px; height: 54px; background: var(--grey);
    display: flex; flex-direction: column; align-items: center; justify-content: center; gap: 3px;
  }
  .brand-name { font-size: 13px; font-weight: 600; color: var(--navy); }
  .brand-tag { font-size: 8px; font-weight: 400; letter-spacing: 1px; color: var(--navy); }

  /* back */
  .focus { left: 43px; top: 766px; width: 240px; font-size: 7px; line-height: 8.4px; }
  .focus h2 { margin: 0 0 6px; font-size: 8.5px; font-weight: 600; color: var(--sky); }
  .focus p { margin: 0 0 9px; }
  .contact { left: 408px; top: 766px; width: 250px; font-size: 7px; line-height: 8.4px; }
  .contact p { margin: 0 0 9px; }
  .contact-dark { left: 43px; top: 1052px; width: 240px; font-size: 7px; line-height: 8.4px; color: var(--sky); }
  .contact-dark p { margin: 0 0 9px; }
  .team-photo { background: linear-gradient(180deg, #2f6fc2 0%, #3a5ea8 55%, #7d8c8a 100%); }
  .truck-photo { background: linear-gradient(180deg, #2c7fd6 0%, #6aa6e0 55%, #5f7f3a 100%); }
  .clinic-photo { background: linear-gradient(160deg, #e8e8e6 0%, #c9ccce 45%, #5b6e7e 75%, #d9dde0 100%); }
</style>
</head>
<body>
<div class="sheet">

  <div class="side-label" style="top:28px;">FRONT</div>
  <section class="front">
    <div class="abs" style="left:0;top:70px;width:724px;height:515px;background:var(--aqua);"></div>
    <div class="abs" style="left:0;top:70px;width:363px;height:346px;background:var(--white);"></div>
    <div class="abs photo" role="img" aria-label="Close-up photo of a dental mirror checking a patient's teeth" style="left:363px;top:70px;width:299px;height:346px;"></div>
    <svg class="abs" style="left:363px;top:70px;" width="363" height="360" aria-hidden="true">
      <line x1="47" y1="346" x2="250" y2="270" stroke="var(--navy)" stroke-width="4"/>
      <circle cx="265" cy="248" r="36" fill="var(--white)" stroke="var(--navy)" stroke-width="6"/>
    </svg>
    <div class="abs" style="left:0;top:416px;width:668px;height:27px;background:var(--navy);"></div>
    <div class="abs" style="left:0;top:448px;width:363px;height:56px;background:var(--grey);"></div>
    <div class="abs" style="left:0;top:503px;width:363px;height:2px;background:var(--navy);"></div>
    <div class="abs brand-box">
      <span class="brand-name">Coastline Wandering Dental Group</span>
      <span class="brand-tag">CARE THAT COMES TO YOU</span>
    </div>

    <div class="abs letter">
      <h1>Dear Principal,</h1>
      <p>We thank you for the time you are taking to review our mobile dental service. Here at Coastline Wandering Dental Group (CWDG), we are committed to ‘bringing the dentist to you’. We are passionate about providing Bulked Billed Oral Health Care to Primary and High Schools, Aged Care Facilities, Corporate Companies and Aboriginal Communities. Within New South Wales, in the past year, we have serviced over 150 schools, and treated a total of 22,014 students so far.</p>
      <p>We are pleased to introduce our service designed to satisfy your student’s dental needs. Our service is cost effective, user friendly and extremely beneficial in providing oral health education and prevention. We offer;</p>
      <p class="gap">• Free Bulk-Billed assessment and treatment to students who qualify for Healthcover “Bright Start Smiles” program; this includes a dental check-up, cleaning &amp; fluoride treatment, sealants, X-rays and fillings.</p>
      <p>• One-on-one Oral Health education from our professional dentists and oral health therapists</p>
      <p>• Complimentary Dental Care Pack comprising of a toothbrush, toothpaste and other products</p>
      <p>• Students also go into the draw to win various prices drawn after the clinic’s visit to the school</p>
      <p>• Provide a referral to the student’s regular dentist for further treatment they may require</p>
      <p class="gap">CWDG operates within accepted best practice models, and as such, is familiar, and without exception complies with the relevant legislation, regulations, Codes and guidelines governing dentistry, including but not limited to, the Dental Code of Conduct for Health Practitioners by the Oral Health Practitioner Board.</p>
      <p>Our mobile dental clinics feature state-of-the-art; oral health equipment and machinery. Including a Dental X-Ray OPG that features low dose radiation, as well as Child Safety Standard Wheel Chair Access. (Please see our website for more information)</p>
      <p>Thank you for considering CWDG, my team and I look forward to providing this free service to your school and most importantly, ‘bringing the dentist to you’.</p>
      <p>Kindest Regards,</p>
      <p class="gap">Marnie Halloway [signature]</p>
      <p>Marketing Manager</p>
    </div>

    <div class="guide" style="left:0;top:70px;width:724px;height:515px;"></div>
    <div class="guide" style="left:8px;top:76px;width:708px;height:503px;"></div>
    <div class="guide-v" style="left:363px;top:70px;height:515px;"></div>
  </section>

  <div class="side-label" style="top:606px;">BACK</div>
  <section class="back">
    <div class="abs" style="left:0;top:650px;width:724px;height:515px;background:var(--white);"></div>
    <div class="abs" style="left:0;top:650px;width:724px;height:41px;background:var(--aqua);"></div>
    <div class="abs" style="left:0;top:698px;width:724px;height:30px;background:var(--navy);"></div>

    <div class="abs focus">
      <h2>“OUR FOCUS IS ON EDUCATION &amp; PREVENTION”</h2>
      <p>“1 in 5 children between the ages of 4-8 years of age will suffer from tooth decay or dental caries as a result of poor dental hygiene” (ref; The Southern College of Child Health)</p>
      <p>Thus, leading to possible dental destruction to their adult teeth. This, in conjunction with diet, lifestyle and social welfare can be contribution to the increase of child absenteeism.</p>
      <p>Book us now for 2015 and help us, bring back your student’s “bright smile”</p>
    </div>

    <div class="abs contact">
      <p>To find out about our procedures or to book your school for 2015 and take advantage of this opportunity, Please visit our website www.cwdg-example.net or email me at marnie.h@cwdg-example.net</p>
      <p>Or to speak to one of our friendly staff, call us directly on (02) 5550 1427<br>In addition, feel free to visit Chatterloop/Chirpwire/Workweave to see regular updates, features, special offers and daily tips regarding our services.</p>
    </div>

    <div class="abs" style="left:0;top:898px;width:363px;height:67px;background:var(--aqua);"></div>
    <div class="abs" style="left:0;top:965px;width:363px;height:180px;background:var(--navy);"></div>
    <div class="abs team-photo" role="img" aria-label="Photo of the dental team in scrubs beside the mobile clinic" style="left:30px;top:925px;width:142px;height:95px;"></div>
    <div class="abs truck-photo" role="img" aria-label="Photo of the mobile dental clinic truck parked on grass" style="left:174px;top:925px;width:141px;height:95px;"></div>
    <div class="abs contact-dark">
      <p>To find out about our procedures or to book your school for 2015 and take advantage of this opportunity, Please visit our website www.cwdg-example.net or email me at marnie.h@cwdg-example.net</p>
      <p>Or to speak to one of our friendly staff, call us directly on (02) 5550 1427<br>In addition, feel free to visit Chatterloop/Chirpwire/Workweave to see regular updates, features, special offers and daily tips regarding our services.</p>
    </div>

    <div class="abs" style="left:363px;top:898px;width:361px;height:247px;background:var(--aqua);"></div>
    <div class="abs clinic-photo" role="img" aria-label="Photo of two dental staff treating a young patient in the mobile clinic chair" style="left:363px;top:903px;width:361px;height:240px;"></div>
    <div class="abs" style="left:0;top:1145px;width:724px;height:20px;background:var(--aqua);"></div>

    <div class="guide" style="left:0;top:650px;width:724px;height:515px;"></div>
    <div class="guide" style="left:8px;top:656px;width:708px;height:503px;"></div>
    <div class="guide-v" style="left:363px;top:650px;height:515px;"></div>
  </section>

</div>
</body>
</html>
```